Set of 6 Icons and buttons required

We have written a windows based app which gives clients access to reports etc.

We are a multichannel epos company

We require 6 buttons and icons along with a suggested font to use and a background for the form.

I have attatched a mock up of what we require from the chosen designer.

The buttons are as follows :

Stockcard ( This is a program which customers can enter stock and check stock levels etc )

Reports ( as the title says )

Stock ( This for making adjustments )

Goods ( this is for booking goods in )

Settings ( As title says )

Help ( As title says )

Dimensions
---------------

The form : 296x268
Buttons : 218x36
Icons on button : 32x32
Text size : Size 10

If you look at the attatched document this is something I put together just to show what we are looking once we put all the components together

Our website is q-ledgora.co.uk

Target Market(s)

B2B

Industry/Entity Type

It Company

```html
<!DOCTYPE html>
<html lang="en">
<head>
<meta charset="utf-8">
<title>q-ledgora – Main Menu</title>
<link href="https://fonts.googleapis.com/css2?family=Open+Sans:wght@400;600&display=swap" rel="stylesheet">
<style>
  :root {
    --frame-border: #c9ccd3;
    --navy-deep: #24286f;
    --navy: #26307f;
    --blue-mid: #1f4fa3;
    --blue-light: #1d86cf;
    --button-top: #ffffff;
    --button-bottom: #d4d4d6;
    --icon-top: #f4f4f4;
    --icon-bottom: #c9c9cb;
    --label: #767676;
    --brand-panel: #2c2a5c;
    --brand-text: #e8e9f2;
    --bar-green: #1e9a3a;
    --arrow-red: #d8262a;
    --doc-blue: #1d64b7;
    --cart-dark: #333;
    --cart-orange: #ef6a1f;
    --cart-wheel: #1f8fd6;
  }
  * { box-sizing: border-box; margin: 0; padding: 0; }
  html, body { width: 1200px; height: 1082px; overflow: hidden; background: #fff; }
  body { font-family: "Open Sans", Arial, sans-serif; }

  .app-form {
    position: relative;
    width: 1200px; height: 1082px;
    border: 3px solid var(--frame-border);
    border-radius: 14px;
    overflow: hidden;
    background: linear-gradient(180deg, var(--navy-deep) 12%, var(--navy) 30%, var(--blue-mid) 70%, var(--blue-light) 100%);
  }
  .title-bar {
    position: absolute; left: 0; top: 0; width: 100%; height: 127px;
    background: linear-gradient(180deg, var(--navy-deep) 0%, #1f4a9a 60%, #1f7cc6 100%);
  }
  .close-button {
    position: absolute; left: 1046px; top: 28px; width: 88px; height: 78px;
    border-radius: 8px;
    background: linear-gradient(180deg, #fafafa, #cfcfd2);
    display: flex; align-items: center; justify-content: center;
  }
  .brand-panel {
    position: absolute; left: 36px; top: 225px; width: 227px; height: 763px;
    background: var(--brand-panel);
    border: 1px solid #1a1940;
    display: flex; flex-direction: column; align-items: center; justify-content: center;
    gap: 18px;
  }
  .brand-mark {
    width: 40px; height: 40px; background: var(--brand-text);
  }
  .brand-name {
    font-size: 34px; font-weight: 400; color: var(--brand-text);
    line-height: 1;
  }
  .menu {
    position: absolute; left: 291px; top: 218px; width: 872px;
    list-style: none;
  }
  .menu-button {
    position: relative; height: 127px; margin-bottom: 3px;
    border-radius: 12px;
    background: linear-gradient(180deg, var(--button-top) 0%, #f1f1f2 45%, var(--button-bottom) 100%);
    display: flex; align-items: center;
  }
  .menu-icon {
    position: absolute; left: 21px; top: 16px; width: 110px; height: 98px;
    border-radius: 8px;
    background: linear-gradient(180deg, var(--icon-top), var(--icon-bottom));
    display: flex; align-items: center; justify-content: center;
  }
  .menu-label {
    position: absolute; left: 174px;
    font-size: 49px; color: var(--label); font-weight: 400;
  }
</style>
</head>
<body>
<main class="app-form">
  <header class="title-bar"></header>
  <div class="close-button" aria-label="Close">
    <svg width="46" height="46" viewBox="0 0 46 46"><path d="M8 8 L38 38 M38 8 L8 38" stroke="#555" stroke-width="9" stroke-linecap="round"/></svg>
  </div>

  <aside class="brand-panel">
    <span class="brand-mark"></span>
    <span class="brand-name">q-ledgora</span>
  </aside>

  <ul class="menu">
    <li class="menu-button">
      <span class="menu-icon">
        <svg width="84" height="76" viewBox="0 0 84 76">
          <g fill="var(--bar-green)">
            <rect x="14" y="58" width="10" height="12"/><rect x="28" y="50" width="10" height="20"/>
            <rect x="42" y="40" width="10" height="30"/><rect x="56" y="30" width="10" height="40"/>
            <rect x="70" y="20" width="10" height="50"/>
          </g>
          <polyline points="4,44 20,30 30,38 46,22 56,28 72,10" fill="none" stroke="var(--arrow-red)" stroke-width="3"/>
          <polygon points="80,4 66,8 76,18" fill="var(--arrow-red)"/>
        </svg>
      </span>
      <span class="menu-label">Stockcard</span>
    </li>
    <li class="menu-button">
      <span class="menu-icon">
        <svg width="70" height="84" viewBox="0 0 70 84">
          <polygon points="10,22 28,4 28,22" fill="#7cc242"/>
          <rect x="10" y="22" width="50" height="60" fill="var(--doc-blue)"/>
          <rect x="28" y="4" width="32" height="18" fill="var(--doc-blue)"/>
          <g stroke="#fff" stroke-width="3">
            <line x1="20" y1="34" x2="50" y2="34"/><line x1="20" y1="43" x2="50" y2="43"/>
            <line x1="20" y1="52" x2="50" y2="52"/><line x1="20" y1="61" x2="50" y2="61"/>
            <line x1="20" y1="70" x2="50" y2="70"/>
          </g>
        </svg>
      </span>
      <span class="menu-label">Reports</span>
    </li>
    <li class="menu-button">
      <span class="menu-icon">
        <svg width="84" height="70" viewBox="0 0 84 70">
          <g fill="var(--bar-green)">
            <rect x="6" y="54" width="11" height="14"/><rect x="22" y="44" width="11" height="24"/>
            <rect x="38" y="34" width="11" height="34"/><rect x="54" y="22" width="11" height="46"/>
            <rect x="70" y="8" width="11" height="60"/>
          </g>
        </svg>
      </span>
      <span class="menu-label">Stock</span>
    </li>
    <li class="menu-button">
      <span class="menu-icon">
        <svg width="84" height="70" viewBox="0 0 84 70">
          <polyline points="4,12 16,12 28,46 70,46" fill="none" stroke="var(--cart-orange)" stroke-width="5"/>
          <polygon points="18,16 80,16 70,42 28,42" fill="var(--cart-dark)"/>
          <circle cx="34" cy="58" r="7" fill="var(--cart-wheel)"/>
          <circle cx="64" cy="58" r="7" fill="var(--cart-wheel)"/>
        </svg>
      </span>
      <span class="menu-label">Goods</span>
    </li>
    <li class="menu-button">
      <span class="menu-icon">
        <svg width="80" height="80" viewBox="0 0 80 80">
          <circle cx="30" cy="30" r="18" fill="none" stroke="var(--arrow-red)" stroke-width="10" stroke-dasharray="7 4.3"/>
          <circle cx="30" cy="30" r="14" fill="var(--arrow-red)"/>
          <circle cx="30" cy="30" r="6" fill="#e6e6e6"/>
          <circle cx="60" cy="58" r="11" fill="none" stroke="var(--bar-green)" stroke-width="7" stroke-dasharray="5 3.6"/>
          <circle cx="60" cy="58" r="8" fill="var(--bar-green)"/>
          <circle cx="60" cy="58" r="3.5" fill="#e6e6e6"/>
        </svg>
      </span>
      <span class="menu-label">Settings</span>
    </li>
    <li class="menu-button">
      <span class="menu-icon">
        <svg width="76" height="76" viewBox="0 0 76 76">
          <circle cx="38" cy="38" r="28" fill="none" stroke="#f2f2f2" stroke-width="16"/>
          <circle cx="38" cy="38" r="28" fill="none" stroke="var(--arrow-red)" stroke-width="16" stroke-dasharray="22 22" stroke-dashoffset="11"/>
          <circle cx="38" cy="38" r="36" fill="none" stroke="#999" stroke-width="1"/>
          <circle cx="38" cy="38" r="20" fill="none" stroke="#999" stroke-width="1"/>
        </svg>
      </span>
      <span class="menu-label">Help</span>
    </li>
  </ul>
</main>
</body>
</html>
```